Business Cards

Business card design for my company.
I would like the card's background colour to be black. You can also see our web site to get an idea of our brand. https://www.dlqmarrowfield.com.au/
- Name
- Email

```html
<!DOCTYPE html>
<html lang="en">
<head>
<meta charset="utf-8">
<title>DLQ Marrowfield – Business Cards</title>
<link rel="stylesheet" href="https://fonts.googleapis.com/css2?family=Montserrat:wght@400;700&family=Roboto:wght@400;500&display=swap">
<style>
  :root {
    --page: #2b2b2d;
    --card-dark: #232325;
    --card-darker: #1a1a1c;
    --brand-green: #0d8f3f;
    --brand-green-light: #14a34c;
    --arc-white: #f2f2f2;
    --text-light: #f4f4f4;
    --text-muted: #d8d8d8;
    --emboss: #3a3a3d;
  }
  * { box-sizing: border-box; margin: 0; padding: 0; }
  html, body { width: 1200px; height: 852px; overflow: hidden; }
  body {
    background: var(--page);
    display: flex;
    align-items: center;
    justify-content: center;
    gap: 40px;
    font-family: "Roboto", Arial, sans-serif;
  }
  .card {
    position: relative;
    width: 540px;
    height: 310px;
    border-radius: 22px;
    overflow: hidden;
    box-shadow: 0 10px 30px rgba(0,0,0,.45);
  }

  /* Front */
  .card--front {
    background: linear-gradient(150deg, var(--card-dark), var(--card-darker));
    border-bottom: 8px solid var(--brand-green);
  }
  .front-brand {
    position: absolute;
    left: 0; right: 0; top: 112px;
    display: flex;
    align-items: center;
    justify-content: center;
    gap: 12px;
    font-family: "Montserrat", Arial, sans-serif;
    font-weight: 700;
    font-size: 32px;
    letter-spacing: 2px;
    color: var(--emboss);
  }
  .front-brand .mark {
    width: 22px; height: 22px;
    background: var(--emboss);
  }
  .front-url {
    position: absolute;
    right: 30px; bottom: 22px;
    font-size: 13px;
    color: var(--text-light);
  }

  /* Back */
  .card--back { background: var(--card-dark); }
  .back-shape { position: absolute; inset: 0; }
  .back-brand {
    position: absolute;
    left: 30px; top: 138px;
    width: 210px;
    font-family: "Montserrat", Arial, sans-serif;
    font-weight: 700;
    font-size: 22px;
    line-height: 1.15;
    letter-spacing: 1px;
    color: #ffffff;
    text-align: center;
  }
  .contact {
    position: absolute;
    left: 292px; top: 70px;
    color: var(--text-light);
  }
  .contact-name {
    font-size: 18px;
    font-weight: 500;
    color: var(--brand-green-light);
    letter-spacing: .3px;
  }
  .contact-title {
    font-size: 12px;
    color: var(--text-muted);
    margin-bottom: 22px;
  }
  .contact-list { list-style: none; }
  .contact-list li {
    display: flex;
    align-items: center;
    gap: 10px;
    font-size: 12px;
    line-height: 20px;
    color: var(--text-light);
  }
  .contact-list svg { width: 12px; height: 12px; fill: var(--text-muted); flex: none; }
</style>
</head>
<body>

  <section class="card card--front" aria-label="Business card front">
    <div class="front-brand"><span class="mark"></span>DLQ MARROWFIELD</div>
    <p class="front-url">www.dlqmarrowfield.com.au</p>
  </section>

  <section class="card card--back" aria-label="Business card back">
    <svg class="back-shape" viewBox="0 0 540 310" preserveAspectRatio="none" aria-hidden="true">
      <path d="M0 55 Q150 40 215 110 Q262 175 268 310 L0 310 Z" fill="var(--arc-white)"/>
      <path d="M0 55 Q140 45 200 112 Q245 175 246 310 L0 310 Z" fill="var(--brand-green)"/>
    </svg>
    <div class="back-brand">DLQ<br>MARROWFIELD</div>

    <div class="contact">
      <h1 class="contact-name">Ross Calder</h1>
      <p class="contact-title">General Manager</p>
      <ul class="contact-list">
        <li><svg viewBox="0 0 24 24"><path d="M6.6 10.8a15.1 15.1 0 0 0 6.6 6.6l2.2-2.2c.3-.3.7-.4 1-.2 1.1.4 2.3.6 3.6.6.6 0 1 .4 1 1V20c0 .6-.4 1-1 1A17 17 0 0 1 3 4c0-.6.4-1 1-1h3.5c.6 0 1 .4 1 1 0 1.3.2 2.5.6 3.6.1.3 0 .7-.2 1z"/></svg>0400 555 183</li>
        <li><svg viewBox="0 0 24 24"><path d="M2 5h20v14H2z M4 7v.5l8 5 8-5V7l-8 5z"/></svg>info@dlqmarrowfield.com.au</li>
        <li><svg viewBox="0 0 24 24"><path d="M12 2a10 10 0 1 0 0 20 10 10 0 0 0 0-20zm0 2c1 1.3 1.8 3 2.1 5H9.9C10.2 7 11 5.3 12 4zM4.3 13a8 8 0 0 1 0-2h3.5a16 16 0 0 0 0 2zm.8 2h3c.3 1.4.8 2.7 1.5 3.8A8 8 0 0 1 5.1 15zm3-6h-3a8 8 0 0 1 4.5-3.8C8.9 6.3 8.4 7.6 8.1 9zM12 20c-1-1.3-1.8-3-2.1-5h4.2c-.3 2-1.1 3.7-2.1 5zm2.3-7H9.7a14 14 0 0 1 0-2h4.6a14 14 0 0 1 0 2zm.1 5.8c.7-1.1 1.2-2.4 1.5-3.8h3a8 8 0 0 1-4.5 3.8zm1.8-5.8a16 16 0 0 0 0-2h3.5a8 8 0 0 1 0 2zM15.9 9c-.3-1.4-.8-2.7-1.5-3.8A8 8 0 0 1 18.9 9z"/></svg>www.dlqmarrowfield.com.au</li>
        <li><svg viewBox="0 0 24 24"><path d="M12 2a7 7 0 0 0-7 7c0 5.3 7 13 7 13s7-7.7 7-13a7 7 0 0 0-7-7zm0 9.5a2.5 2.5 0 1 1 0-5 2.5 2.5 0 0 1 0 5z"/></svg>Kingston, Tasmania, Australia</li>
      </ul>
    </div>
  </section>

</body>
</html>
```